Tovi Sarrow Systems Web Site

I need website designed for Tovi Sarrow Systems, LLC. It is an email marketing software as a service business. I am looking for a five page website with the ability to accept payments. I have included our logo below for integration with the website. I do not have the text ready yet.

The domain to use is tovi-sarrow.com

I have also included some examples of other websites that outline the basic structure I would like
https://usebluntfern.com/
https://www.postbrim.com/

I know I need to provide some more information, but I want to get the ball rolling and see what is needed.
Thanks!
Dirk

```html
<!DOCTYPE html>
<html lang="en">
<head>
<meta charset="utf-8">
<title>Tovi Sarrow Systems — Email Marketing Software</title>
<link rel="stylesheet" href="https://fonts.googleapis.com/css2?family=Poppins:wght@300;400;500;600;700&display=swap">
<style>
:root{
  --navy:#2c2470;
  --navy-deep:#241d60;
  --ink:#2f3848;
  --text:#666a75;
  --red:#f2130f;
  --sky:#d3ebfb;
  --blue:#3fa2ee;
  --brand:#74aee6;
  --white:#ffffff;
}
*{margin:0;padding:0;box-sizing:border-box}
html,body{width:1200px;height:2367px;overflow:hidden}
body{position:relative;background:var(--white);font-family:"Poppins",sans-serif;color:var(--ink)}
.abs{position:absolute}
a{color:inherit;text-decoration:none}

/* hero */
.hero-blob{left:0;top:0}
.brand{left:182px;top:24px;width:160px;text-align:center}
.brand-mark{width:70px;height:70px;border-radius:50%;border:3px solid var(--brand);margin:0 auto 10px}
.brand-name{font-size:17px;font-weight:400;color:var(--brand);letter-spacing:.5px;white-space:nowrap}
.nav{left:0;top:0;width:1200px;height:100px;z-index:2;font-size:11.5px;font-weight:400;color:var(--ink)}
.nav a{position:absolute;top:58px;white-space:nowrap;line-height:14px}
.nav .active{color:var(--red)}
.nav .login{font-weight:500;color:#111}
.nav .signup{top:50px;left:1001px;width:92px;height:29px;background:var(--blue);color:var(--white);border-radius:15px;display:flex;align-items:center;justify-content:center;line-height:1}
.cloud{background:var(--sky);border-radius:30px;z-index:1}
.monitor{left:182px;top:160px;width:474px;height:430px;border-radius:8px;background:linear-gradient(160deg,#e9ecef 0%,#cfd5dc 60%,#b8c0c8 100%)}
.monitor-screen{left:196px;top:176px;width:446px;height:260px;background:linear-gradient(135deg,#8fd0f7 0%,#5fb0ec 60%,#4a7fb8 100%)}
.screen-text{left:242px;top:240px;color:var(--white);font-size:28px;font-weight:700;line-height:36px}
.hero-title{left:684px;top:222px;font-size:37px;font-weight:700;line-height:42px;color:var(--ink);letter-spacing:.5px}
.hero-copy{left:684px;top:310px;width:350px;font-size:13px;line-height:22px;color:#4a4f5c}
.btn{display:flex;align-items:center;justify-content:center;background:var(--red);color:var(--white);font-weight:600;border-radius:24px}
.hero-btn{left:687px;top:373px;width:137px;height:36px;font-size:13px}
.arrow{width:26px;height:26px;border-radius:50%;display:flex;align-items:center;justify-content:center}
.arrow-prev{left:12px;top:314px;background:#2b2b2b}
.arrow-next{left:1162px;top:314px;background:#8a8d93}

/* features */
.feature{width:300px;text-align:center}
.feature-icon{height:70px;display:flex;justify-content:center;align-items:flex-end}
.feature h3{margin-top:16px;font-size:16px;font-weight:600;color:#222}
.feature p{margin-top:14px;font-size:12.5px;line-height:23.5px;color:var(--text);font-weight:300}
.feature .more{display:inline-block;margin-top:14px;font-size:13px;font-weight:500;color:#222;text-decoration:underline}

/* promo band */
.promo{left:0;top:1075px;width:1200px;height:453px;background:var(--navy)}
.promo-title{left:191px;top:1175px;width:560px;font-size:37px;font-weight:600;line-height:59px;color:var(--white)}
.promo-btn{left:191px;top:1372px;width:174px;height:48px;font-size:17px}
.promo-photo{left:774px;top:1022px;width:394px;height:506px;border-radius:120px 120px 0 0;background:linear-gradient(180deg,#4a5f8e 0%,#3b5a8f 45%,#c9ccd1 78%,#aeb3ba 100%)}

/* about */
.about-rule{left:190px;top:1622px;width:47px;height:3px;background:var(--red)}
.about-label{left:250px;top:1613px;font-size:13px;font-weight:500;color:var(--ink)}
.about-title{left:191px;top:1643px;width:360px;font-size:24px;font-weight:500;line-height:35px;color:#2d3550}
.about-copy{left:605px;top:1642px;width:420px;font-size:11.5px;line-height:20px;color:#737782;font-weight:300}
.about-copy p+p{margin-top:16px}

/* footer */
.footer{left:0;top:1904px;width:1200px;height:463px;background:var(--navy)}
.footer-deco{left:740px;top:1920px;width:450px;height:450px;border-radius:50%;border:14px solid rgba(255,255,255,.06)}
.footer h4{font-size:14px;font-weight:600;color:var(--white);letter-spacing:.3px}
.contact-col{left:200px;top:2000px;color:var(--white)}
.contact-row{display:flex;align-items:flex-start;font-size:12px;line-height:22px}
.contact-row svg{flex:none;margin-right:14px;margin-top:3px}
.links{font-size:12.5px;color:var(--white);line-height:20px}
.links a{display:block;margin-bottom:22px}
.footer-rule{left:150px;top:2260px;width:900px;height:1px;background:rgba(255,255,255,.18)}
.copyright{left:191px;top:2282px;font-size:10.5px;color:var(--white);font-weight:300}
.social{left:886px;top:2279px;display:flex}
.social span{width:17px;height:17px;border-radius:50%;background:var(--white);margin-right:24px}
.social span:nth-child(2){background:#2aa3ef}
</style>
</head>
<body>

<!-- hero -->
<svg class="abs hero-blob" width="620" height="610" viewBox="0 0 620 610" aria-hidden="true">
  <path d="M0 0H426C520 80 612 250 600 400C592 505 560 578 470 598C300 622 120 578 0 560Z" fill="var(--navy)"/>
</svg>

<div class="abs brand">
  <div class="brand-mark"></div>
  <div class="brand-name">TOVI SARROW</div>
</div>

<div class="abs cloud" style="left:1108px;top:32px;width:92px;height:76px;border-radius:40px 0 0 40px"></div>
<div class="abs cloud" style="left:752px;top:126px;width:70px;height:44px"></div>
<div class="abs cloud" style="left:1016px;top:414px;width:72px;height:46px"></div>
<div class="abs cloud" style="left:794px;top:474px;width:72px;height:46px"></div>

<nav class="abs nav">
  <a class="active" href="#" style="left:526px">HOME</a>
  <a href="#" style="left:588px">FEATURES</a>
  <a href="#" style="left:668px">PLANS &amp; PRICING</a>
  <a href="#" style="left:787px">SERVICES</a>
  <a href="#" style="left:863px">CONTACT</a>
  <a class="login" href="#" style="left:942px">LOGIN</a>
  <a class="signup" href="#">SIGN UP</a>
</nav>

<div class="abs monitor" role="img" aria-label="Desktop computer with keyboard and mouse showing an email marketing illustration with a rocket and a man at a laptop"></div>
<div class="abs monitor-screen" aria-hidden="true"></div>
<div class="abs screen-text">Simplify your<br>email<br>marketing<br>now.</div>

<div class="abs arrow arrow-prev"><svg width="10" height="10" viewBox="0 0 10 10"><path d="M6.5 1.5L3 5l3.5 3.5" stroke="#fff" stroke-width="2" fill="none"/></svg></div>
<div class="abs arrow arrow-next"><svg width="10" height="10" viewBox="0 0 10 10"><path d="M3.5 1.5L7 5 3.5 8.5" stroke="#fff" stroke-width="2" fill="none"/></svg></div>

<h1 class="abs hero-title">Email Marketing<br>Software</h1>
<p class="abs hero-copy">Lorem ipsum dolor sit amet consectetur &nbsp;adipiscing elit, posuere fringilla donec convallis.</p>
<a class="abs btn hero-btn" href="#">Explore Now</a>

<!-- features -->
<section class="abs feature" style="left:150px;top:738px">
  <div class="feature-icon">
    <svg width="68" height="68" viewBox="0 0 68 68"><circle cx="34" cy="34" r="31" fill="none" stroke="var(--red)" stroke-width="2.5"/></svg>
  </div>
  <h3>Simple Interface</h3>
  <p>Leverage agile frameworks to provide<br>a robust synopsis for high level<br>overviews. Iterative approaches<br>Organically</p>
  <a class="more" href="#">Read More</a>
</section>

<section class="abs feature" style="left:450px;top:738px">
  <div class="feature-icon">
    <svg width="66" height="70" viewBox="0 0 66 70">
      <path d="M10 30A23 23 0 0 1 50 16" fill="none" stroke="var(--red)" stroke-width="6"/>
      <path d="M56 40A23 23 0 0 1 16 54" fill="none" stroke="var(--red)" stroke-width="6"/>
      <path d="M44 6l12 10-14 4z" fill="var(--red)"/>
      <path d="M22 64L10 54l14-4z" fill="var(--red)"/>
      <circle cx="33" cy="35" r="15" fill="none" stroke="var(--red)" stroke-width="3"/>
      <text x="33" y="43" text-anchor="middle" font-family="Poppins,sans-serif" font-size="22" font-weight="700" fill="var(--red)">$</text>
    </svg>
  </div>
  <h3>Affordable Pricing</h3>
  <p>Leverage agile frameworks to provide<br>a robust synopsis for high level<br>overviews. Iterative approaches<br>Organically</p>
  <a class="more" href="#">Read More</a>
</section>

<section class="abs feature" style="left:748px;top:738px">
  <div class="feature-icon">
    <svg width="60" height="64" viewBox="0 0 60 64">
      <rect x="4" y="2" width="30" height="58" rx="5" fill="var(--red)"/>
      <rect x="8" y="10" width="22" height="40" fill="#fff"/>
      <path d="M22 30l20-14 14 20-20 14z" fill="var(--red)" stroke="#fff" stroke-width="2"/>
      <path d="M23 31l17 6 2-20" fill="none" stroke="#fff" stroke-width="2"/>
    </svg>
  </div>
  <h3>Responsive Support</h3>
  <p>Leverage agile frameworks to provide<br>a robust synopsis for high level<br>overviews. Iterative approaches<br>Organically</p>
  <a class="more" href="#">Read More</a>
</section>

<!-- promo band -->
<div class="abs promo"></div>
<div class="abs promo-photo" role="img" aria-label="Young man in a denim shirt working on a laptop"></div>
<h2 class="abs promo-title">Learn how easy it is to boost your business with our email marketing software today.</h2>
<a class="abs btn promo-btn" href="#">Explore Now</a>

<!-- about -->
<div class="abs about-rule"></div>
<div class="abs about-label">About Us</div>
<h2 class="abs about-title">Our intuitive drag-and-drop editor makes designing the perfect email faster with real-time collaboration and in-app commenting.</h2>
<div class="abs about-copy">
  <p>Distinctively exploit optimal alignments for intuitive bandwidth. Quickly coordinate e-business applications through revolutionary catalysts for chang the Seamlessly underwhelm optimal testing procedures whereas processes.Synergistically evolve 2.0 technologies rather than just in</p>
  <p>time initiatives. Quickly deploy strategic networks with compelling e-business. Credibly pontificate highly efficient manufactured products and enabled data.Dynamically target high-payoff intellectual capital for customized technologies objectively integrate .</p>
</div>

<!-- footer -->
<footer class="abs footer"></footer>
<div class="abs footer-deco" aria-hidden="true"></div>

<div class="abs contact-col">
  <h4 style="margin-left:29px;margin-bottom:14px">CONTACT</h4>
  <div class="contact-row">
    <svg width="16" height="20" viewBox="0 0 16 20"><path d="M8 1a7 7 0 0 0-7 7c0 5 7 11 7 11s7-6 7-11a7 7 0 0 0-7-7z" fill="#fff"/><circle cx="8" cy="8" r="3" fill="var(--navy)"/></svg>
    <div>TOVI SARROW<br>Kestrel Lane 42<br>20814 Maryland</div>
  </div>
  <div class="contact-row" style="margin-top:14px;font-size:14px">
    <svg width="16" height="16" viewBox="0 0 16 16"><path d="M3 1l3 3-1.5 2.5a10 10 0 0 0 5 5L12 10l3 3-2 2C7 15 1 9 1 3z" fill="#fff"/></svg>
    <div>+1 555 014 2290</div>
  </div>
  <div class="contact-row" style="margin-top:12px">
    <svg width="16" height="12" viewBox="0 0 16 12"><rect x="0" y="0" width="16" height="12" fill="#fff"/><path d="M0 0l8 7 8-7" fill="none" stroke="var(--navy)" stroke-width="1.5"/></svg>
    <div>info@tovisarrow.tech</div>
  </div>
</div>

<h4 class="abs" style="left:480px;top:2000px;font-size:14px;font-weight:600;color:#fff">QUICK LINK</h4>
<div class="abs links" style="left:480px;top:2036px">
  <a href="#">Home</a><a href="#">Features</a><a href="#">Plans &amp; Pricing</a><a href="#">Services</a>
</div>
<div class="abs links" style="left:652px;top:2036px">
  <a href="#">Contact</a><a href="#">Login</a><a href="#">Sign Up</a>
</div>

<div class="abs footer-rule"></div>
<div class="abs copyright">© 2018 TOVI SARROW. All rights reserved.</div>
<div class="abs social" aria-label="Social links"><span></span><span></span><span></span><span></span></div>

</body>
</html>
```